Designing HTML Email Creative

Hi There,
The goal of this project is to design an HTML Email Creative.
Target Market: Minority Women 25 - 45. Low Household incomes. Stay at home moms. Middle America
Subject of Email Campaign: Top 5 Reasons To Go Back to College
The goal is to make the users Buy the top 5 reasons to go back to school and then Get Matched to Online & Local Colleges.
Call to action: Get Matched to Online & Local Colleges
You can add two buttons, one above the reasons and one below. The text in the button should be: Get Matched to Online & Local Colleges Now!
Your goal is to make the call to action in the email pop out so that users know very easily where to click to visit our site.
Please find attached the copy that is to be used in the creative.
Also, the information needs to be sourced so you can create very small links in the bottom of the email.
Also, we just need the psd file for this. Does not need to be coded.
Also, you can find some successful email creative attached so you have an idea.
Please note that we have updated the word doc with the correct content.
Women 25 - 50 - Low Household Incomes - Middle America
School

```html
<!DOCTYPE html>
<html lang="en">
<head>
<meta charset="utf-8">
<title>Top Reasons to Go Back to College</title>
<link rel="stylesheet" href="https://fonts.googleapis.com/css2?family=Cinzel:wght@400;700&family=Noto+Serif&family=PT+Sans:wght@700&family=Arimo:wght@400;700&display=swap">
<style>
:root{
  --page:#ffffff;
  --card-edge:#d9dde3;
  --blue-deep:#0b3fc4;
  --blue-mid:#1c63e6;
  --blue-light:#8fb8f5;
  --gold:#f2b21a;
  --gold-dark:#c98a06;
  --heading-blue:#1b3fb8;
  --body-grey:#4a4a4a;
  --text:#222222;
  --red:#e0261a;
  --btn-top:#f5622e;
  --btn-bottom:#c81408;
  --footer-band:#e7eaee;
  --link:#1a4fbf;
  --ref:#333333;
  --art-tone:#d8dbe0;
  --art-tone-dark:#b9bec6;
  --photo-tone:#e6e2df;
  --photo-tone-blue:#b7cde6;
}
*{margin:0;padding:0;box-sizing:border-box}
html,body{width:714px;height:1200px;overflow:hidden;background:var(--page)}
.stage{position:absolute;left:0;top:0;width:750px;height:1260px;transform:scale(0.952);transform-origin:0 0;font-family:"Arimo",Arial,sans-serif;color:var(--text)}
.card{position:absolute;left:15px;top:10px;width:720px;height:1042px;border:1px solid var(--card-edge);background:#fff;overflow:hidden}
.hero{position:absolute;left:0;top:0;width:720px;height:300px;background:linear-gradient(160deg,var(--blue-light) 0%,var(--blue-mid) 35%,var(--blue-deep) 70%,var(--blue-mid) 100%)}
.hero-curve{position:absolute;left:0;top:0}
.hero-art{position:absolute;left:20px;top:75px;width:320px;height:195px;border-radius:8px;background:linear-gradient(180deg,var(--art-tone) 0%,var(--art-tone-dark) 100%)}
.hero-title{position:absolute;left:330px;top:42px;width:350px;text-align:center;font-family:"Cinzel",serif;color:#fff}
.hero-title .line1{font-size:37px;letter-spacing:2px;line-height:42px}
.hero-title .line2{font-size:23px;letter-spacing:2px;line-height:30px}
.hero-title .line3{font-size:61px;font-weight:700;line-height:74px;color:var(--gold);text-shadow:0 2px 0 var(--gold-dark)}
.portrait{position:absolute;left:485px;top:195px;width:212px;height:207px;background:linear-gradient(180deg,var(--photo-tone) 0%,var(--photo-tone) 55%,var(--photo-tone-blue) 100%)}
.intro{position:absolute;left:40px;top:305px;width:400px}
.intro h1{font-family:"Noto Serif",serif;font-weight:400;font-size:34px;color:var(--heading-blue);line-height:42px}
.intro p{margin-top:8px;font-size:16px;line-height:26px;color:var(--body-grey)}
.cta{position:absolute;left:160px;width:402px;height:46px;border-radius:23px;background:linear-gradient(180deg,var(--btn-top) 0%,var(--red) 50%,var(--btn-bottom) 100%);box-shadow:0 3px 4px rgba(0,0,0,.3);color:#fff;font-family:"PT Sans",sans-serif;font-weight:700;font-size:18px;line-height:46px;text-align:center;text-decoration:none}
.cta-top{top:425px}
.cta-bottom{top:913px}
.reasons{position:absolute;left:42px;top:507px;width:630px;list-style:none}
.reason{margin-bottom:13px}
.reason h2{font-weight:400;font-size:14.5px;color:var(--red);line-height:20px;margin-bottom:3px}
.reason p{font-size:12.5px;letter-spacing:.25px;line-height:20px;color:var(--text)}
.reason b{font-weight:700}
.footer-band{position:absolute;left:0;top:990px;width:720px;height:52px;background:linear-gradient(180deg,#fff 0%,var(--footer-band) 100%);text-align:center;font-size:15px;line-height:52px;color:#333}
.footer-band a{color:var(--link);font-weight:700;text-decoration:none}
.sources{position:absolute;left:36px;top:1080px;width:690px;font-size:10px;line-height:17px;color:var(--ref);list-style:none}
.sources li{margin-bottom:5px}
.sources a{color:var(--link);text-decoration:none}
</style>
</head>
<body>
<div class="stage">
  <div class="card">
    <div class="hero">
      <svg class="hero-curve" width="720" height="300" viewBox="0 0 720 300">
        <path d="M0 150 C180 130 320 240 720 255 L720 300 L0 300 Z" fill="#ffffff"/>
      </svg>
      <div class="hero-art" role="img" aria-label="Graduation cap with tassel resting on a rolled diploma tied with a red ribbon"></div>
      <div class="hero-title">
        <div class="line1">TOP REASONS</div>
        <div class="line2">TO GO BACK TO</div>
        <div class="line3">COLLEGE</div>
      </div>
    </div>
    <div class="portrait" role="img" aria-label="Photo of a smiling young woman wearing a blue scarf and white top"></div>

    <div class="intro">
      <h1>Empower Yourself!</h1>
      <p>Empower yourself!&nbsp; Education frees you financially and boosts your self-esteem and self-confidence.</p>
    </div>

    <a class="cta cta-top" href="#">Get Matched to Online &amp; Local Colleges Now</a>

    <ol class="reasons">
      <li class="reason">
        <h2>1. Education Pays – Make Double the Money</h2>
        <p>College grads <b>earn nearly twice as much</b> as those with only high school diplomas.&nbsp; Median weekly salary with <b>high school diploma, $652</b>.&nbsp; Median weekly salary with <b>Bachelor’s degree $1,066</b>.</p>
      </li>
      <li class="reason">
        <h2>2.&nbsp; Government Grants – Federal Access Grants</h2>
        <p>College is more affordable than you think.&nbsp; <b>Federal Access Grants of up to $5,550</b> are available to qualifying students.&nbsp; Grants are free money, which does not have to be paid back.&nbsp; Other Federal and state grants are also available, as are low cost government loans and countless scholarships.</p>
      </li>
      <li class="reason">
        <h2>3. Lower Unemployment Rates for College Grads.</h2>
        <p>High school graduates 8.3% unemployed, college graduates 4.5 % unemployed.</p>
      </li>
      <li class="reason">
        <h2>4. Make $1 Million More in Lifetime – Retirement Security</h2>
        <p>On average, those with a <b>bachelor’s degree earn a $1 million</b> more in their lifetime than those with a high school diploma.</p>
      </li>
      <li class="reason">
        <h2>5.&nbsp; Be More Employable</h2>
        <p>Of the 2 million plus job added during the recent U.S. economic recovery, the majorities were for college graduates.</p>
      </li>
    </ol>

    <a class="cta cta-bottom" href="#">Get Matched to Online &amp; Local Colleges Now</a>

    <div class="footer-band">You with a college degree—oh the places you will go.&nbsp; <a href="#">Click here</a> to explore the possibilities.</div>
  </div>

  <ul class="sources">
    <li>Education Pays," National Workforce Data Office, January 28&nbsp; 2013.&nbsp; Accessed April 21, 2013 &lt;<a href="#">www.workforcedata.example/earnings-chart.htm</a>&gt;</li>
    <li>"Access Grants" Student Aid Center--An Office of the National Education Board. Accessed April 21, 2013.<br>&lt;<a href="#">http://studentaidcenter.example/grants/access</a>&gt;</li>
    <li>"Education Pays," National Workforce Data Office, January 28&nbsp; 2013.&nbsp; Accessed April 21, 2013 &lt;<a href="#">www.workforcedata.example/earnings-chart.htm</a>&gt;</li>
    <li>National Survey Bureau, October 2012. Accessed April 20, 2013. &lt;<a href="#">www.surveybureau.example/2012/report-04.pdf</a>&gt;</li>
    <li>Harlow, Renee. "What is a College Education Worth?" Mind Matters Weekly, August 16 2012.&nbsp; Accessed April 20, 2013.<br>&lt;<a href="#">www.mindmattersweekly.example/blog/good-thinking/college-education-worth</a>&gt;</li>
  </ul>
</div>
</body>
</html>
```